2024 Harwick Patrol Deputy's Statute Handbook

Cover, spine and back cover for our annual law manual. The overall size of the cover is 18.82 x 11 (with the .25 inch bleed it is 19.32 x 11.5) and the spine is 1.82 x 11 plus (1.82 x 11.5 with the bleed).
The book comes with a motor vehicle companion guide which will be 5" X 7" with spiral binding. The companion guide will have the same design with a slight twist related to motor vehicle law.

```html
<!DOCTYPE html>
<html lang="en">
<head>
<meta charset="utf-8">
<title>Patrol Deputy's Statute Handbook – Cover and Companion Guide</title>
<link href="https://fonts.googleapis.com/css2?family=Anton&family=Oswald:wght@400;500;600&family=Open+Sans:wght@400&display=swap" rel="stylesheet">
<style>
  :root{
    --stage:#e8e5e0;
    --royal:#2539ab;
    --spine:#2336a3;
    --band:#151a36;
    --gold:#eab326;
    --white:#ffffff;
    --ink-soft:#dfe5ff;
    --lead:#d8def5;
  }
  *{margin:0;padding:0;box-sizing:border-box;}
  html,body{width:1200px;height:600px;overflow:hidden;background:var(--stage);}
  .canvas{position:relative;width:1200px;height:600px;}

  /* ---------- full wrap: back, spine, front ---------- */
  .wrap{position:absolute;left:36px;top:36px;width:853px;height:500px;background:var(--royal);overflow:hidden;box-shadow:0 2px 6px rgba(0,0,0,.25);}
  .back{position:absolute;left:0;top:0;width:386px;height:500px;background:linear-gradient(90deg,#263cb0 0%,#2236a6 100%);}
  .back-copy{position:absolute;top:74px;left:40px;display:flex;gap:19px;}
  .back-col{width:146px;font-family:"Open Sans",sans-serif;font-size:7.6px;line-height:9.1px;color:var(--ink-soft);text-align:justify;}
  .back-col p+p{margin-top:9px;}
  .back-col.second{width:142px;}

  .spine{position:absolute;left:386px;top:0;width:81px;height:500px;background:var(--spine);}
  .spine-year{position:absolute;top:78px;left:0;width:81px;text-align:center;font-family:"Oswald",sans-serif;font-weight:600;font-size:13px;color:var(--gold);}
  .spine-title{position:absolute;left:40px;top:376px;transform-origin:0 0;transform:rotate(-90deg) translateY(-50%);white-space:nowrap;font-family:"Anton",sans-serif;font-size:18.5px;letter-spacing:.2px;color:var(--white);text-shadow:2px 2px 0 #111a44;}

  .front{position:absolute;left:467px;top:0;width:386px;height:500px;}
  .front-art{position:absolute;inset:0;background:
      linear-gradient(180deg,rgba(18,24,70,.92) 0%,rgba(40,30,90,.7) 14%,rgba(32,52,160,.5) 30%,rgba(37,57,171,.9) 60%,var(--royal) 100%),
      linear-gradient(90deg,#1a2160 0%,#1a2160 58%,#7a2a55 62%,#7a2a55 100%);}
  .title{position:absolute;left:30px;top:76px;color:var(--white);font-family:"Anton",sans-serif;text-shadow:2px 2px 0 rgba(10,14,50,.6);white-space:nowrap;}
  .title-kicker{font-size:36px;line-height:40px;}
  .year{color:var(--gold);}
  .title-main{font-size:44px;line-height:52px;letter-spacing:.3px;}

  .brand{position:absolute;display:flex;align-items:center;gap:4px;font-family:"Oswald",sans-serif;font-weight:600;color:var(--gold);white-space:nowrap;}
  .brand .dot{width:10px;height:10px;border-radius:50%;background:var(--gold);}
  .brand.front-mark{left:300px;top:322px;font-size:13px;}

  .band{position:absolute;left:0;top:388px;width:853px;height:54px;background:var(--band);}
  .band-lead{position:absolute;left:494px;top:5px;width:177px;text-align:right;font-family:"Oswald",sans-serif;font-weight:500;font-size:19px;line-height:22px;color:var(--lead);white-space:nowrap;}
  .band-list{position:absolute;left:683px;top:8px;font-family:"Oswald",sans-serif;font-weight:500;font-size:7.8px;line-height:9.6px;letter-spacing:.9px;color:var(--white);list-style:none;white-space:nowrap;}
  .brand.band-mark{left:768px;top:20px;font-size:12px;}
  .brand.spine-mark{left:394px;top:20px;font-size:11px;}
  .author{position:absolute;left:467px;top:454px;width:386px;text-align:center;font-family:"Oswald",sans-serif;font-weight:500;font-size:16px;color:var(--white);}

  /* ---------- companion guide ---------- */
  .guide{position:absolute;left:912px;top:186px;width:253px;height:350px;background:var(--royal);overflow:hidden;box-shadow:0 2px 6px rgba(0,0,0,.25);}
  .guide-art{position:absolute;inset:0;background:
      linear-gradient(180deg,rgba(18,24,70,.92) 0%,rgba(40,30,90,.7) 14%,rgba(32,52,160,.5) 40%,rgba(37,57,171,.9) 70%,var(--royal) 100%),
      linear-gradient(90deg,#1a2160 0%,#1a2160 56%,#7a2a55 60%,#7a2a55 100%);}
  .guide-title{position:absolute;left:0;top:54px;width:253px;text-align:center;color:var(--white);font-family:"Anton",sans-serif;text-shadow:2px 2px 0 rgba(10,14,50,.6);white-space:nowrap;}
  .guide-title .title-kicker{font-size:20px;line-height:25px;}
  .guide-title .title-main{font-size:34px;line-height:34px;}
  .brand.guide-mark{left:190px;top:212px;font-size:11px;}
  .guide-band{position:absolute;left:0;top:274px;width:253px;height:40px;background:var(--band);}
  .guide-lead{position:absolute;left:8px;top:6px;width:178px;text-align:center;font-family:"Oswald",sans-serif;font-weight:500;font-size:10.5px;color:var(--lead);white-space:nowrap;}
  .guide-sub{position:absolute;left:8px;top:22px;width:178px;text-align:center;font-family:"Oswald",sans-serif;font-weight:500;font-size:7px;letter-spacing:.8px;color:var(--white);white-space:nowrap;}
  .brand.guide-band-mark{left:190px;top:14px;font-size:11px;}
</style>
</head>
<body>
<div class="canvas">

  <section class="wrap" aria-label="Book cover wrap">
    <div class="back">
      <div class="back-copy">
        <div class="back-col">
          <p>Lorem ipsum dolor sit amet, consectetur adipiscing elit. Nunc vel massa ut sem luctus ornare vel at elit. Nunc massa elit, facilisis ac ligula tempus, consequat suscipit arcu. Nunc eget pharetra nulla. Etiam lobortis odio et ex fringilla, id pretium turpis consectetur. Nulla cursus, odio vel sollicitudin vestibulum, massa urna mollis ante, et posuere ante turpis sed sapien. Aenean at nunc at sapien elementum lacinia eget sit amet mauris. Suspendisse ut consequat dui. Aliquam erat volutpat. Praesent venenatis facilisis ornare. Sed eu erat leo. Sed nec odio id quam sodales ornare eget eget metus. Cras dapibus velit lectus, sit amet pellentesque orci sagittis faucibus.</p>
          <p>Cras dapibus nec diam ut finibus. Sed nec hendrerit magna. Mauris enim nisi, finibus id turpis at, auctor aliquam tellus. Maecenas scelerisque at dui quis</p>
        </div>
        <div class="back-col second">
          <p>faucibus. Fusce orci mi, accumsan sit amet faucibus rutrum, mattis sollicitudin risus. Nunc ullamcorper purus ut enim placerat rhoncus. Etiam in ipsum dui.</p>
          <p>Etiam lobortis lectus vel nibh lacinia, quis facilisis quam elementum. Mauris scelerisque lobortis odio. Sed eu turpis commodo, varius lorem vitae, elementum magna. Ut lacinia massa dui, a porttitor ante tempor eget. Nam eget lobortis metus. Integer ultrices dapibus pretium. Phasellus sit amet rhoncus enim. Nunc tempor nisi justo, in placerat enim luctus a. Vivamus in elit lectus. Nunc eget massa suscipit, vestibulum massa nec, scelerisque eros.</p>
        </div>
      </div>
    </div>

    <div class="spine">
      <div class="spine-year">2024</div>
      <div class="spine-title">PATROL DEPUTY'S STATUTE HANDBOOK</div>
    </div>

    <div class="front">
      <div class="front-art" role="img" aria-label="Weathered American flag painted on a brick wall above two uniformed officers at night, tinted blue"></div>
      <div class="title">
        <div class="title-kicker">PATROL DEPUTY'S <span class="year">2024</span></div>
        <div class="title-main">STATUTE HANDBOOK</div>
      </div>
      <div class="brand front-mark"><span class="dot"></span>CORLISS</div>
    </div>

    <div class="band">
      <div class="band-lead">Harwick patrol<br>deputy's guide to:</div>
      <ul class="band-list">
        <li>CRIMINAL PROCEDURE</li>
        <li>STATUTORY LAW</li>
        <li>MOTOR VEHICLE LAW</li>
        <li>JUVENILE LAW</li>
      </ul>
      <div class="brand band-mark"><span class="dot"></span>CORLISS</div>
      <div class="brand spine-mark"><span class="dot"></span>CORLISS</div>
    </div>

    <div class="author">Daniel R. Corliss, ESQ</div>
  </section>

  <section class="guide" aria-label="Motor vehicle companion guide cover">
    <div class="guide-art" role="img" aria-label="Weathered American flag on brick above a police cruiser with lights at night, tinted blue"></div>
    <div class="guide-title">
      <div class="title-kicker">PATROL DEPUTY'S <span class="year">2024</span></div>
      <div class="title-main">MOTOR VEHICLE<br>GUIDE</div>
    </div>
    <div class="brand guide-mark"><span class="dot"></span>CORLISS</div>
    <div class="guide-band">
      <div class="guide-lead">Harwick patrol deputy's guide to:</div>
      <div class="guide-sub">MOTOR VEHICLES LAW AND RULES</div>
      <div class="brand guide-band-mark"><span class="dot"></span>CORLISS</div>
    </div>
  </section>

</div>
</body>
</html>
```